Distinctinctive and nordic inspired container design for a new started health and active brand.

Our company name is MORO and stands for "Move onward, Reach Outward". Our goal is to provide a no BS approach to Supplementation and specific problem solving products.

As a Danish based brand our key words is: "Minimalism", "clear lines", "Nordic colours i.eg. and as seen in canvas", "Purity", "simplicity", "design", "Functionality", "health", "clarity" and "calm".

This design is aimed at a two container product (AM) for "night" and (PM) for "day".
Design is focused on a rectangular shape with a rectangular shape lid that screws on to a uniform and harmonious design.
Colour wise we are most into matte "earth colors that can also be seen in canvas.
These can be singular or a mix in the design but we kindly ask to stay away from "bright and shiny" colours.
Logos and scriptures will be added as a 2D effect, with exception for the lid logo which we would to see retracted into the lid itself.

In a rendering design we would like two containers next to each other seen from different angles where one lid is screwed off and one is screwed on.
In addition we would like a single container rendering showing only PM and only AM.

Happy designing

Pieter & Rasmus - MORO

Target Market(s)

European and North american markets.
Target: Male and Female age group 18-50.

Industry/Entity Type

Health Product

Font styles to use
Serif
Sans Serif

Requirements
Must have
• Clear and distinctive profile
Matte colours
uniform and harmonious shape (rectangular base)
inspired by earth minerals colours and contours.
Nice to have
• 3D visual effect in rendering to better get a feel of the product
Should not have
• Shiny colours or material indicators.

```html
<!DOCTYPE html>
<html lang="en">
<head>
<meta charset="utf-8">
<title>MORO – Night (AM) and Day (PM) container labels</title>
<link rel="stylesheet" href="https://fonts.googleapis.com/css2?family=Russo+One&family=PT+Sans+Narrow:wght@400;700&family=Arimo:ital,wght@0,400;0,700;1,400&display=swap">
<style>
  :root {
    --page: #f4f4f3;
    --night-ground: #3b352c;
    --night-ink: #e6e1d9;
    --night-accent: #b39d80;
    --night-rule: #e6e1d9;
    --day-ground: #cdc4b7;
    --day-ink: #2d3231;
    --day-accent: #4a4237;
    --day-rule: #2d3231;
  }
  * { margin: 0; padding: 0; box-sizing: border-box; }
  html, body { width: 725px; height: 1200px; overflow: hidden; background: var(--page); }
  .canvas { position: relative; width: 725px; height: 1200px; }

  .label {
    position: absolute;
    width: 141px;
    height: 388px;
    border-radius: 6px;
    overflow: hidden;
    background: var(--ground);
    color: var(--ink);
  }
  .label.night { --ground: var(--night-ground); --ink: var(--night-ink); --accent: var(--night-accent); --rule: var(--night-rule); --band-ink: var(--night-ground); }
  .label.day { --ground: var(--day-ground); --ink: var(--day-ink); --accent: var(--day-accent); --rule: var(--day-rule); --band-ink: var(--day-ground); }

  .row-night .label { top: 157px; }
  .row-day .label { top: 722px; }
  .col-back { left: 90px; }
  .col-front { left: 289px; }
  .col-story { left: 489px; }

  /* brand mark stand-in */
  .brand-mark {
    position: absolute; top: 34px; left: 0; right: 0;
    display: flex; align-items: center; justify-content: center; gap: 5px;
    font-family: "Russo One", sans-serif; font-size: 15px; color: var(--accent);
    letter-spacing: 1px;
  }
  .brand-mark .square { width: 8px; height: 8px; background: var(--accent); }

  /* nutrition panel */
  .nutrition {
    position: absolute; top: 87px; left: 17px; width: 108px;
    border: 1px solid var(--rule); padding: 3px 5px 3px;
    font-family: "Arimo", sans-serif; font-size: 4.3px; line-height: 1.45;
    color: var(--ink);
  }
  .nutrition h3 { font-family: "Arimo", sans-serif; font-weight: 700; font-size: 11px; line-height: 1.1; }
  .nutrition .row { display: flex; justify-content: space-between; border-top: 0.5px solid var(--rule); }
  .nutrition .row.plain { border-top: none; }
  .nutrition .bar { height: 3px; background: var(--rule); margin: 1px 0; }
  .nutrition .indent { padding-left: 8px; }
  .nutrition b { font-weight: 700; }
  .nutrition .dv { text-align: right; font-size: 3.4px; font-weight: 700; }
  .nutrition .note { font-size: 3.4px; line-height: 1.3; border-top: 0.5px solid var(--rule); padding-top: 1px; }
  .nutrition .end { height: 1.5px; background: var(--rule); margin-top: 2px; }

  .ingredients-title {
    position: absolute; top: 277px; left: 0; right: 0; text-align: center;
    font-family: "Russo One", sans-serif; font-size: 12px; color: var(--accent);
    letter-spacing: 0.3px;
  }
  .ingredients-text {
    position: absolute; top: 296px; left: 15px; right: 15px; text-align: center;
    font-family: "PT Sans Narrow", sans-serif; font-size: 6px; line-height: 8.8px;
  }
  .web {
    position: absolute; top: 350px; left: 0; right: 0; text-align: center;
    font-family: "PT Sans Narrow", sans-serif; font-weight: 700; font-size: 8.5px;
  }

  /* front panel */
  .front-name {
    position: absolute; left: 59px; top: 200px;
    transform: translate(-50%, -50%) rotate(-90deg);
    font-family: "Russo One", sans-serif; font-size: 74px; line-height: 1;
    color: var(--ink); white-space: nowrap; letter-spacing: 1px;
  }
  .front-square {
    position: absolute; left: 52px; top: 48px; width: 14px; height: 14px; background: var(--accent);
  }
  .tagline {
    position: absolute; left: 107px; top: 200px;
    transform: translate(-50%, -50%) rotate(-90deg);
    font-family: "Russo One", sans-serif; font-size: 10.5px; text-transform: uppercase;
    color: var(--accent); white-space: nowrap; letter-spacing: 0.2px;
  }
  .time-icon { position: absolute; left: 58px; top: 326px; width: 26px; height: 26px; }
  .time-band {
    position: absolute; top: 357px; left: 2px; right: 2px; height: 12px;
    background: var(--accent); color: var(--band-ink);
    font-family: "Russo One", sans-serif; font-size: 8px; line-height: 12px; text-align: center;
  }

  /* story panel */
  .story-title {
    position: absolute; top: 98px; left: 0; right: 0; text-align: center;
    font-family: "Russo One", sans-serif; color: var(--ink); line-height: 1;
  }
  .story-title .name { display: block; font-size: 31px; letter-spacing: 1px; }
  .story-title .purpose { display: block; font-size: 17px; margin-top: 4px; color: var(--accent); }
  .label.night .story-title .purpose { color: var(--ink); }
  .story-text {
    position: absolute; top: 168px; left: 16px; right: 16px;
    font-family: "PT Sans Narrow", sans-serif; font-size: 6px; line-height: 8.9px;
    text-align: justify; text-align-last: center;
  }
  .motto {
    position: absolute; top: 306px; left: 0; right: 0; text-align: center;
    font-family: "Russo One", sans-serif; font-size: 17px; line-height: 18px;
    color: var(--accent);
  }
</style>
</head>
<body>
<main class="canvas">

  <section class="row-night">
    <article class="label night col-back">
      <div class="brand-mark"><span class="square"></span>MORO</div>
      <div class="nutrition">
        <h3>Nutrition Facts</h3>
        <div class="row plain"><span>Serving Size</span><span>...g</span></div>
        <div class="row plain"><span>Servings Per Container</span></div>
        <div class="bar"></div>
        <div class="row plain"><b>Amount Per Serving</b></div>
        <div class="row"><span><b>Calories</b> ....</span><span>Calories from Fat ...</span></div>
        <div class="row dv"><span></span><span>% Daily Value*</span></div>
        <div class="row"><span><b>Total Fat</b> ...g</span><b>...%</b></div>
        <div class="row indent"><span>Saturated Fat ...g</span><b>...%</b></div>
        <div class="row indent"><span><i>Trans</i> Fat ...g</span></div>
        <div class="row"><span><b>Cholestrol</b> ...mg</span><b>...%</b></div>
        <div class="row"><span><b>Sodium</b> ...mg</span><b>...%</b></div>
        <div class="row"><span><b>Total Carbohydrate</b> ...g</span><b>...%</b></div>
        <div class="row indent"><span>Dietary Fiber ...g</span><b>...%</b></div>
        <div class="row indent"><span>Sugars ...g</span></div>
        <div class="row"><span><b>Protein</b> ...g</span></div>
        <div class="bar"></div>
        <div class="row plain"><span>Vitamin A</span><b>...%</b></div>
        <div class="row"><span>Vitamin C</span><b>...%</b></div>
        <div class="row"><span>Calcium</span><b>...%</b></div>
        <div class="row"><span>Iron</span><b>...%</b></div>
        <div class="note">*Percent Daily Values are based on a 2,000 calorie diet. Your Daily Values may be higer or lower depending on your calorie needs.</div>
        <div class="end"></div>
      </div>
      <h2 class="ingredients-title">INGREDIENTS</h2>
      <p class="ingredients-text">Lorem Ipsum is simply dummy text of the printing and typesetting industry. Lorem Ipsum has been the industry's standard dummy text ever since the 1500s, when an unknown printer took a galley of type and scrambled it to make a type specimen book.</p>
      <p class="web">www.websiteaddress.com</p>
    </article>

    <article class="label night col-front">
      <span class="front-square"></span>
      <h1 class="front-name">MORO</h1>
      <p class="tagline">Move onward, Reach Outward</p>
      <svg class="time-icon" viewBox="0 0 26 26" aria-hidden="true">
        <path d="M14 3a10 10 0 1 0 9 14a8 8 0 1 1 -9 -14z" fill="var(--accent)"/>
        <circle cx="19" cy="8" r="1.3" fill="var(--accent)"/>
        <circle cx="22" cy="12" r="1.1" fill="var(--accent)"/>
      </svg>
      <div class="time-band">NIGHT(AM)</div>
    </article>

    <article class="label night col-story">
      <div class="brand-mark"><span class="square"></span>MORO</div>
      <h2 class="story-title"><span class="name">MORO</span><span class="purpose">PURPOSE</span></h2>
      <p class="story-text">Lorem Ipsum is simply dummy text of the printing and typesetting industry. Lorem Ipsum has been the industry's standard dummy text ever since the 1500s, when an unknown printer took a galley of type and scrambled it to make a type specimen book. It has survived not only five centuries, but also the leap into electronic typesetting, remaining essentially unchanged. It was popularised in the 1960s with the release of Letraset sheets containing Lorem Ipsum passages, and more recently with desktop publishing software like Aldus PageMaker including versions of Lorem Ipsum.</p>
      <p class="motto">LIVE<br>YOUR<br>BEST</p>
    </article>
  </section>

  <section class="row-day">
    <article class="label day col-back">
      <div class="brand-mark"><span class="square"></span>MORO</div>
      <div class="nutrition">
        <h3>Nutrition Facts</h3>
        <div class="row plain"><span>Serving Size</span><span>...g</span></div>
        <div class="row plain"><span>Servings Per Container</span></div>
        <div class="bar"></div>
        <div class="row plain"><b>Amount Per Serving</b></div>
        <div class="row"><span><b>Calories</b> ....</span><span>Calories from Fat ...</span></div>
        <div class="row dv"><span></span><span>% Daily Value*</span></div>
        <div class="row"><span><b>Total Fat</b> ...g</span><b>...%</b></div>
        <div class="row indent"><span>Saturated Fat ...g</span><b>...%</b></div>
        <div class="row indent"><span><i>Trans</i> Fat ...g</span></div>
        <div class="row"><span><b>Cholestrol</b> ...mg</span><b>...%</b></div>
        <div class="row"><span><b>Sodium</b> ...mg</span><b>...%</b></div>
        <div class="row"><span><b>Total Carbohydrate</b> ...g</span><b>...%</b></div>
        <div class="row indent"><span>Dietary Fiber ...g</span><b>...%</b></div>
        <div class="row indent"><span>Sugars ...g</span></div>
        <div class="row"><span><b>Protein</b> ...g</span></div>
        <div class="bar"></div>
        <div class="row plain"><span>Vitamin A</span><b>...%</b></div>
        <div class="row"><span>Vitamin C</span><b>...%</b></div>
        <div class="row"><span>Calcium</span><b>...%</b></div>
        <div class="row"><span>Iron</span><b>...%</b></div>
        <div class="note">*Percent Daily Values are based on a 2,000 calorie diet. Your Daily Values may be higer or lower depending on your calorie needs.</div>
        <div class="end"></div>
      </div>
      <h2 class="ingredients-title">INGREDIENTS</h2>
      <p class="ingredients-text">Lorem Ipsum is simply dummy text of the printing and typesetting industry. Lorem Ipsum has been the industry's standard dummy text ever since the 1500s, when an unknown printer took a galley of type and scrambled it to make a type specimen book.</p>
      <p class="web">www.websiteaddress.com</p>
    </article>

    <article class="label day col-front">
      <span class="front-square"></span>
      <h1 class="front-name">MORO</h1>
      <p class="tagline">Move onward, Reach Outward</p>
      <svg class="time-icon" viewBox="0 0 26 26" aria-hidden="true">
        <circle cx="13" cy="13" r="6" fill="var(--accent)"/>
        <g stroke="var(--accent)" stroke-width="1.6" stroke-linecap="round">
          <line x1="13" y1="1.5" x2="13" y2="4.5"/><line x1="13" y1="21.5" x2="13" y2="24.5"/>
          <line x1="1.5" y1="13" x2="4.5" y2="13"/><line x1="21.5" y1="13" x2="24.5" y2="13"/>
          <line x1="4.9" y1="4.9" x2="7" y2="7"/><line x1="19" y1="19" x2="21.1" y2="21.1"/>
          <line x1="4.9" y1="21.1" x2="7" y2="19"/><line x1="19" y1="7" x2="21.1" y2="4.9"/>
        </g>
      </svg>
      <div class="time-band">DAY(PM)</div>
    </article>

    <article class="label day col-story">
      <div class="brand-mark"><span class="square"></span>MORO</div>
      <h2 class="story-title"><span class="name">MORO</span><span class="purpose">PURPOSE</span></h2>
      <p class="story-text">Lorem Ipsum is simply dummy text of the printing and typesetting industry. Lorem Ipsum has been the industry's standard dummy text ever since the 1500s, when an unknown printer took a galley of type and scrambled it to make a type specimen book. It has survived not only five centuries, but also the leap into electronic typesetting, remaining essentially unchanged. It was popularised in the 1960s with the release of Letraset sheets containing Lorem Ipsum passages, and more recently with desktop publishing software like Aldus PageMaker including versions of Lorem Ipsum.</p>
      <p class="motto">LIVE<br>YOUR<br>BEST</p>
    </article>
  </section>

</main>
</body>
</html>
```